Cat-products company needs smart, yet endearing, business card

We need a business card design for a new, but up-and-running, business based in Honolulu, Hawaii. The business is Purrlane Nest Co. Our first product is the most environmentally-friendly cat grass kit ever seen on the planet. Future products, currently in the R&D phase, will include a variety of exciting cat scratchers. We also do consulting work to help apartment-dwellers make their home more cat-friendly and, in the future, plan on doing full, custom installs of structure to create high walkways for cats.

Target Market(s)

Middle-aged, apartment-dwelling, middle-class workers who own 1 or more cats and who dote on them.

Industry/Entity Type

Pet Care

Contact Information for Business Card

A striking, professional, yet warm and friendly design is what we're after.

Font styles to use
Serif
Sans Serif
Other font styles liked:
• Comfortaa

Colors

Designer to choose colors to be used in the design.

Requirements
Must have
• The company logo: (see attachment)
• The company name: Purrlane Nest Co
• The web address: www.purrlanenestco.example
• Email: support@purrlanenestco.example
• Phone: +1 (808) 555 0172
• Update (Fri Jun 30 3017 7:45pm Hawaii Time) I would like, is possible, uploaded picture of the cat grass kit on the back of the card with some text along the lines of: Purrlane Nest Co - Where The Freshest Kitty Sprouts Begin
Nice to have
• A cat picture, cartoon, real or silhouette that illustrates cats in action and/or relaxing; ie using the apartment space to live, play and relax in and being well-contented.
• Most of the website is done in the font: Comfortaa. It might be nice to continue using this for brand consistency.
Should not have
• Hard-to-read fonts.

```html
<!DOCTYPE html>
<html lang="en">
<head>
<meta charset="utf-8">
<title>Purrlane Nest Co – Business Card</title>
<link rel="stylesheet" href="https://fonts.googleapis.com/css2?family=Comfortaa:wght@400;700&display=swap">
<style>
  :root {
    --stage: #86700d;
    --card: #2e1d28;
    --gold: #f5b324;
    --brown: #5a3a2e;
    --rule: #d9648a;
    --icon: #7a1a24;
    --muted: #c9a8b4;
    --frame: #ffffff;
    --pattern-a: #3a2a52;
    --pattern-b: #332238;
    --grass-a: #7fa64a;
    --grass-b: #8a6a45;
  }
  * { margin: 0; padding: 0; box-sizing: border-box; }
  html, body {
    width: 1200px; height: 1200px; overflow: hidden;
    background: var(--stage);
    font-family: "Comfortaa", sans-serif;
  }
  .canvas { position: relative; width: 1200px; height: 1200px; }

  .card {
    position: absolute;
    width: 840px; height: 480px;
    background: var(--card);
    overflow: hidden;
  }
  .card--front { left: 54px; top: 105px; }
  .card--back  { left: 273px; top: 644px; }

  .damask {
    position: absolute; inset: 0;
    background: radial-gradient(circle at 30% 40%, var(--pattern-a), var(--pattern-b) 70%);
  }

  .frame {
    position: absolute;
    border: 3px solid var(--frame);
    background: var(--card);
  }
  .card--front .frame { left: 50px; top: 45px; width: 734px; height: 398px; }
  .card--back .frame  { left: 73px; top: 155px; width: 732px; height: 197px; }

  /* Front */
  .holder__name {
    position: absolute; left: 0; top: 46px; width: 682px;
    text-align: center; font-size: 24px; line-height: 28px; color: var(--gold);
  }
  .holder__first { color: var(--brown); }
  .holder__role {
    position: absolute; left: 0; top: 80px; width: 652px;
    text-align: center; font-size: 13px; line-height: 16px; color: var(--muted);
  }
  .divider {
    position: absolute; left: 71px; top: 105px;
    width: 589px; height: 2px; background: var(--rule);
  }
  .mascot {
    position: absolute; left: 614px; top: 44px;
    width: 68px; height: 60px;
    background: linear-gradient(135deg, #a47a45, #6b4a2a);
    border-radius: 12px 12px 6px 6px;
  }

  .contacts { position: absolute; left: 86px; top: 166px; list-style: none; }
  .contacts__item {
    display: flex; align-items: center;
    height: 20px; font-size: 13px; color: var(--gold);
  }
  .contacts__item + .contacts__item { margin-top: 39px; }
  .contacts__item:nth-child(3) { margin-top: 33px; }
  .contacts__icon { width: 16px; height: 16px; margin-right: 32px; flex: none; }

  .brand-mark {
    position: absolute; left: 576px; top: 196px; width: 150px;
    text-align: center; color: var(--gold);
    font-weight: 700; font-size: 18px; line-height: 22px;
  }
  .brand-mark__dot {
    display: block; width: 36px; height: 36px; margin: 0 auto 10px;
    border-radius: 50%; background: var(--brown);
  }

  .footer-name {
    position: absolute; left: 0; width: 708px; top: 371px;
    text-align: center; font-size: 18px; line-height: 22px; color: var(--gold);
  }

  /* Back */
  .kit-photo {
    position: absolute; left: 36px; top: 28px;
    width: 140px; height: 135px; border-radius: 6px;
    background: linear-gradient(160deg, var(--grass-a), var(--grass-b));
  }
  .back-mark {
    position: absolute; left: 190px; right: 20px; top: 22px;
    display: flex; flex-direction: column; align-items: center;
    color: var(--gold); text-align: center;
  }
  .back-mark__dot {
    width: 48px; height: 48px; border-radius: 50%;
    background: var(--brown); margin-bottom: 12px;
  }
  .back-mark__name { font-weight: 700; font-size: 36px; line-height: 42px; }
  .back-mark__tagline {
    margin-top: 14px; font-size: 14px; line-height: 18px; color: var(--muted);
  }
</style>
</head>
<body>
<div class="canvas">

  <section class="card card--front">
    <div class="damask" role="img" aria-label="Blue line-drawn floral damask pattern on deep plum"></div>
    <div class="frame">
      <p class="holder__name"><span class="holder__first">Mara</span> Kealoha</p>
      <p class="holder__role">CEO</p>
      <div class="divider"></div>
      <div class="mascot" role="img" aria-label="Illustration of a sitting tabby cat"></div>

      <ul class="contacts">
        <li class="contacts__item">
          <svg class="contacts__icon" viewBox="0 0 16 16"><path fill="var(--icon)" d="M3.5 1l2.5 3-1.5 1.5c.8 2 2.5 3.7 4.5 4.5L10.5 8.5l3 2.5-1.5 3C7 14 2 9 2 2.5z"/></svg>
          +1 (808) 555 0172
        </li>
        <li class="contacts__item">
          <svg class="contacts__icon" viewBox="0 0 16 16"><rect x="1" y="3" width="14" height="10" fill="var(--icon)"/><path d="M1 3l7 6 7-6" fill="none" stroke="var(--card)" stroke-width="1"/></svg>
          support@purrlanenestco.example
        </li>
        <li class="contacts__item">
          <svg class="contacts__icon" viewBox="0 0 16 16" fill="none" stroke="var(--icon)" stroke-width="1.2"><circle cx="8" cy="8" r="6.5"/><ellipse cx="8" cy="8" rx="3" ry="6.5"/><path d="M1.5 8h13M2.5 5h11M2.5 11h11"/></svg>
          www.purrlanenestco.example
        </li>
      </ul>

      <div class="brand-mark">
        <span class="brand-mark__dot"></span>
        Purrlane Nest Co
      </div>

      <p class="footer-name">Purrlane Nest Co</p>
    </div>
  </section>

  <section class="card card--back">
    <div class="damask" role="img" aria-label="Blue line-drawn floral damask pattern on deep plum"></div>
    <div class="frame">
      <div class="kit-photo" role="img" aria-label="Photo of the cat grass kit with fresh green sprouts"></div>
      <div class="back-mark">
        <span class="back-mark__dot"></span>
        <p class="back-mark__name">Purrlane Nest Co</p>
        <p class="back-mark__tagline">Purrlane Nest Co - Where The Freshest Kitty Sprouts Begin</p>
      </div>
    </div>
  </section>

</div>
</body>
</html>
```